Property developer, money partner needs business card design using logo concept provided

Our company develops residential properties, does money lends for joint ventures in property deals and finds property deals for other money partners. We have provided a basic logo for you to work from. Any graphic or logo design on the card is to communicate development and finance collaboration. Color choice is not so important for us, but color choice does need to reflect professionalism.

```html
<!DOCTYPE html>
<html lang="en">
<head>
<meta charset="utf-8">
<title>Keystone Property Partners – Business Card</title>
<link rel="stylesheet" href="https://fonts.googleapis.com/css2?family=Montserrat:wght@700&family=Open+Sans:wght@400;600&display=swap">
<style>
  :root{
    --stage:#232323;
    --card:#1e1f23;
    --band-mid:#25262b;
    --band-low:#2c2d32;
    --red:#b3191f;
    --blue:#1a6fd0;
    --white:#f4f4f4;
    --muted:#c9c9cc;
  }
  *{margin:0;padding:0;box-sizing:border-box}
  html,body{width:1200px;height:780px;overflow:hidden;background:var(--stage)}
  .stage{position:relative;width:1200px;height:780px}
  .card{position:absolute;top:92px;width:340px;height:595px;border-radius:22px;overflow:hidden;background:var(--card);box-shadow:0 18px 40px rgba(0,0,0,.55)}
  .card--back{left:200px}
  .card--front{left:660px}

  .back-pattern{position:absolute;inset:0;background:linear-gradient(135deg,#5d5e62 0%,#2a2b2f 38%,#1b1c20 70%,#15161a 100%)}
  .back-mark{position:absolute;top:130px;left:210px;display:flex;align-items:center;gap:6px}
  .back-mark .dot{width:14px;height:14px;border-radius:50%;background:var(--blue)}
  .back-mark .name{font:700 8px 'Montserrat',sans-serif;color:var(--white);letter-spacing:.5px;text-transform:uppercase}

  .bands{position:absolute;inset:0}
  .band{filter:drop-shadow(0 8px 10px rgba(0,0,0,.45))}

  .brand{position:absolute;top:70px;left:0;width:100%;text-align:center}
  .brand .dot{width:70px;height:70px;border-radius:50%;background:var(--blue);margin:0 auto 16px}
  .brand .name{font:700 19px 'Montserrat',sans-serif;color:var(--white);letter-spacing:3px;text-transform:uppercase;line-height:1.2}
  .brand .reg{font:400 8px 'Open Sans',sans-serif;color:var(--muted);letter-spacing:2px;margin-top:6px}

  .person{position:absolute;top:258px;left:0;width:100%;text-align:center}
  .person .full{font:700 32px 'Montserrat',sans-serif;line-height:1}
  .person .first{color:var(--red)}
  .person .last{color:var(--white)}
  .person .role{font:600 15px 'Open Sans',sans-serif;color:var(--white);margin-top:8px}

  .icons{position:absolute;top:340px;left:0;width:100%;display:flex;justify-content:center;gap:10px}
  .icon{width:26px;height:26px;border-radius:50%;background:var(--red);display:flex;align-items:center;justify-content:center}
  .icon svg{width:14px;height:14px}

  .contact{position:absolute;top:378px;left:0;width:100%;text-align:center;font:400 15px/1.45 'Open Sans',sans-serif;color:var(--white)}

  .address{position:absolute;top:492px;left:0;width:100%;text-align:center;font:400 15px/1.4 'Open Sans',sans-serif;color:var(--white)}
  .address .icon{margin:0 auto 8px}
</style>
</head>
<body>
<main class="stage">

  <section class="card card--back" aria-label="Card back">
    <div class="back-pattern" role="img" aria-label="Repeating pattern of the company mark in glossy and matte black"></div>
    <div class="back-mark">
      <span class="dot"></span>
      <span class="name">Keystone</span>
    </div>
  </section>

  <section class="card card--front" aria-label="Card front">
    <svg class="bands" viewBox="0 0 340 595" width="340" height="595" aria-hidden="true">
      <rect width="340" height="595" fill="var(--band-low)"/>
      <path class="band" d="M0 0H340V455Q250 510 40 545L0 552Z" fill="var(--band-mid)"/>
      <path class="band" d="M0 0H340V330Q300 455 60 470L0 468Z" fill="var(--card)"/>
    </svg>

    <header class="brand">
      <div class="dot"></div>
      <div class="name">Keystone<br>Property Partners</div>
      <div class="reg">A.C.N 418 203 556</div>
    </header>

    <div class="person">
      <div class="full"><span class="first">Elena</span> <span class="last">Varga</span></div>
      <div class="role">Co-Founder</div>
    </div>

    <div class="icons">
      <span class="icon"><svg viewBox="0 0 24 24" fill="#fff"><path d="M6.6 10.8a15 15 0 0 0 6.6 6.6l2.2-2.2a1 1 0 0 1 1-.25 11.4 11.4 0 0 0 3.6.57 1 1 0 0 1 1 1V20a1 1 0 0 1-1 1A17 17 0 0 1 3 4a1 1 0 0 1 1-1h3.5a1 1 0 0 1 1 1c0 1.25.2 2.45.57 3.57a1 1 0 0 1-.25 1z"/></svg></span>
      <span class="icon"><svg viewBox="0 0 24 24" fill="none" stroke="#fff" stroke-width="2"><rect x="3" y="5" width="18" height="14" rx="2"/><path d="M3 7l9 6 9-6"/></svg></span>
      <span class="icon"><svg viewBox="0 0 24 24" fill="none" stroke="#fff" stroke-width="2"><circle cx="12" cy="12" r="9"/><path d="M3 12h18M12 3c3 3 3 15 0 18M12 3c-3 3-3 15 0 18"/></svg></span>
    </div>

    <div class="contact">
      <div>(555) 214-0387</div>
      <div>hello@keystonepp.com</div>
      <div>www.keystonepp.com</div>
    </div>

    <div class="address">
      <span class="icon"><svg viewBox="0 0 24 24" fill="#fff"><path d="M12 2a7 7 0 0 0-7 7c0 5 7 13 7 13s7-8 7-13a7 7 0 0 0-7-7zm0 9.5A2.5 2.5 0 1 1 12 6.5a2.5 2.5 0 0 1 0 5z"/></svg></span>
      <div>740 Harbor Lane, Suite 12</div>
      <div>Millbrook, TX 75001</div>
    </div>
  </section>

</main>
</body>
</html>
```